VFX Company Business Card Design Project

The Ember Vale is a decentralized Visual Effects Studio servicing the television and feature film industries.
Project Brief:
Take our logo that was previously designed on Pixel Harbor and make a double sided business card.
Requirements:
- Card MUST be double sided.
- Front of card MUST have the yellow part of our logo against the dark grey background.
- Back of card is completely up to the designer.
- Back of card must include the complete company logo.
Please follow these File Preparation guidelines:
http://printmoor.example/infopage?file=filetype_en&s=PrintMoor_new&lang=en
Industry/Entity Type
Business
Look and feel
Each slider illustrates characteristics of the customer's brand and the style your logo design should communicate.

```html
<!DOCTYPE html>
<html lang="en">
<head>
<meta charset="utf-8">
<title>The Ember Vale – Business Card</title>
<link rel="stylesheet" href="https://fonts.googleapis.com/css2?family=Josefin+Sans:wght@300;400;600;700&display=swap">
<style>
  :root {
    --page-bg: #ffffff;
    --card-bg: #262626;
    --brand-yellow: #fdc72a;
    --detail-yellow: #e4b22c;
    --muted-yellow: #b88f2a;
    --card-shadow: rgba(0, 0, 0, 0.45);
  }
  * { margin: 0; padding: 0; box-sizing: border-box; }
  html, body {
    width: 1200px;
    height: 900px;
    overflow: hidden;
    background: var(--page-bg);
    font-family: "Josefin Sans", sans-serif;
  }
  .canvas {
    position: relative;
    width: 1200px;
    height: 900px;
  }
  .card {
    position: absolute;
    left: 311px;
    width: 635px;
    height: 317px;
    background: var(--card-bg);
    box-shadow: 0 5px 6px var(--card-shadow);
  }
  .card--front { top: 118px; }
  .card--back { top: 480px; }

  .front-name {
    position: absolute;
    inset: 0;
    display: flex;
    align-items: center;
    justify-content: center;
    color: var(--brand-yellow);
    font-weight: 700;
    font-size: 62px;
    letter-spacing: 1px;
  }

  .brand {
    position: absolute;
    left: 44px;
    top: 128px;
    display: flex;
    align-items: center;
    gap: 12px;
    color: var(--brand-yellow);
    font-weight: 700;
    font-size: 27px;
  }
  .brand-dot {
    width: 22px;
    height: 22px;
    border-radius: 50%;
    background: var(--brand-yellow);
  }

  .contact {
    position: absolute;
    right: 33px;
    top: 30px;
    bottom: 18px;
    text-align: right;
  }
  .contact-name {
    color: var(--brand-yellow);
    font-weight: 700;
    font-size: 20px;
    line-height: 1.1;
  }
  .contact-title {
    color: var(--brand-yellow);
    font-weight: 600;
    font-size: 16px;
    letter-spacing: 1.5px;
    margin-top: 3px;
  }
  .contact-address {
    margin-top: 96px;
    color: var(--detail-yellow);
    font-weight: 300;
    font-size: 16.5px;
    line-height: 22px;
    letter-spacing: 0.5px;
  }
  .contact-lines {
    margin-top: 20px;
    color: var(--muted-yellow);
    font-weight: 300;
    font-size: 17px;
    line-height: 22px;
    letter-spacing: 0.5px;
  }
  .contact-web {
    position: absolute;
    right: 0;
    bottom: 0;
    color: var(--brand-yellow);
    font-weight: 600;
    font-size: 16px;
    letter-spacing: 3px;
    white-space: nowrap;
  }
</style>
</head>
<body>
<main class="canvas">
  <section class="card card--front" aria-label="Card front">
    <div class="front-name">The Ember Vale</div>
  </section>

  <section class="card card--back" aria-label="Card back">
    <div class="brand">
      <span class="brand-dot"></span>
      <span class="brand-name">The Ember Vale</span>
    </div>

    <div class="contact">
      <div class="contact-name">MARCUS HALE</div>
      <div class="contact-title">Creative Director</div>
      <address class="contact-address" style="font-style:normal">
        2290 Linden Ridge Ave<br>
        Halton, ON L7K 4R2
      </address>
      <div class="contact-lines">
        mhale@embervale.example<br>
        T/M (555) 214-0386
      </div>
      <div class="contact-web">www.embervale.example</div>
    </div>
  </section>
</main>
</body>
</html>
```